Letterhead Design for Law Firm that Specializes in Property Damage Litigation

We are looking for a redesign of our letterhead. Our current letterhead lists all of our current staff members and we'd like to come up with a design that does NOT list all of the staff members so that it does not need to be updated with every newly hired employee. Must be in editable format.

We are a law firm that specializes in property damage, so we need something that is professional, yet modern. The final design should use our existing logo and should use a blue color scheme (alternate colors would be gray, black, and white).

Industry/Entity Type

Legal

Colors
0054AA
0677BA
7BADD7
CADEEF
E8F1F8

```html
<!DOCTYPE html>
<html lang="en">
<head>
<meta charset="utf-8">
<title>Hartwell Ames &amp; Corbin — Letterhead</title>
<link href="https://fonts.googleapis.com/css2?family=Open+Sans:wght@400;600;700&family=Raleway:wght@600;700&family=Mrs+Saint+Delafield&display=swap" rel="stylesheet">
<style>
  :root {
    --backdrop: #e4e4e0;
    --paper: #fdfdf4;
    --blue: #2c5d9c;
    --navy: #1f4a80;
    --grey-mark: #8c8c8c;
    --text-strong: #555a5e;
    --text-body: #9a9c9c;
    --text-soft: #a3a5a5;
    --rule: #e2e2d6;
    --icon: #2b2b2b;
  }
  * { margin: 0; padding: 0; box-sizing: border-box; }
  html, body { width: 1043px; height: 1200px; overflow: hidden; }
  body { background: var(--backdrop); font-family: "Open Sans", Arial, sans-serif; position: relative; }

  .letterhead {
    position: absolute; left: 90px; top: 75px; width: 783px; height: 1012px;
    background: var(--paper);
  }

  .brand { position: absolute; left: 64px; top: 70px; width: 262px; }
  .brand-row { display: flex; align-items: center; gap: 12px; }
  .brand-square { width: 26px; height: 26px; background: var(--blue); flex: none; }
  .brand-name {
    color: var(--blue); font-weight: 600; font-size: 22px; line-height: 26px;
    letter-spacing: 1px; text-transform: uppercase;
  }
  .brand-tagline {
    margin-top: 12px; font-size: 10.5px; letter-spacing: 2.4px; color: var(--grey-mark);
    font-weight: 600; white-space: nowrap;
  }

  .header-divider { position: absolute; left: 343px; top: 58px; width: 1px; height: 133px; background: var(--rule); }

  .office { position: absolute; top: 74px; }
  .office--pa { left: 361px; }
  .office--nj { left: 572px; }
  .office-title { color: var(--blue); font-weight: 700; font-size: 12.5px; margin-bottom: 9px; }
  .office-line { display: flex; align-items: center; gap: 8px; font-size: 11.5px; color: var(--text-soft); height: 18px; }
  .office-address { display: flex; gap: 8px; font-size: 9.5px; line-height: 14px; color: var(--text-soft); margin-top: 9px; }
  .office-address svg { flex: none; margin-top: 1px; }

  .recipient { position: absolute; left: 65px; top: 238px; }
  .recipient-name { font-family: "Raleway", "Open Sans", sans-serif; font-weight: 700; font-size: 16.5px; color: var(--text-strong); margin-bottom: 8px; }
  .recipient-line { font-size: 11.5px; line-height: 16.5px; color: var(--text-soft); }

  .letter-body { position: absolute; left: 65px; top: 368px; width: 590px; }
  .letter-body p { font-size: 11.9px; line-height: 16.5px; color: var(--text-body); text-align: justify; margin-bottom: 16.5px; }

  .sign-off { position: absolute; left: 65px; top: 788px; }
  .signature { font-family: "Mrs Saint Delafield", cursive; font-size: 34px; color: var(--text-strong); line-height: 36px; }
  .signer-name { font-family: "Raleway", "Open Sans", sans-serif; font-weight: 700; font-size: 14.5px; color: var(--text-strong); margin-top: 2px; }
  .signer-role { font-size: 11.5px; color: var(--text-soft); margin-top: 4px; }

  .footer-rule { position: absolute; left: 0; top: 936px; width: 592px; height: 3px; background: var(--rule); }
  .footer-rule--right { left: 662px; top: 981px; width: 121px; }
  .footer-square { position: absolute; left: 614px; top: 950px; width: 22px; height: 22px; background: var(--blue); }
  .footer-contacts { position: absolute; left: 68px; top: 957px; display: flex; gap: 24px; }
  .footer-item { display: flex; align-items: center; gap: 7px; font-size: 14px; font-weight: 600; color: var(--navy); }
</style>
</head>
<body>
<main class="letterhead">
  <div class="brand">
    <div class="brand-row">
      <span class="brand-square"></span>
      <div class="brand-name">Hartwell<br>Ames &amp;<br>Corbin</div>
    </div>
    <div class="brand-tagline">THE PROPERTY DAMAGE ATTORNEYS</div>
  </div>

  <div class="header-divider"></div>

  <section class="office office--pa">
    <h2 class="office-title">PHILADELPHIA</h2>
    <div class="office-line">
      <svg width="11" height="11" viewBox="0 0 11 11"><rect width="11" height="11" rx="1.5" fill="var(--icon)"/><path d="M6.8 2.5c-1.8 0.4-2.6 1.7-2.6 3s0.8 2.6 2.6 3" stroke="#fff" stroke-width="1.4" fill="none"/></svg>
      (215) 555-0140
    </div>
    <div class="office-line">
      <svg width="11" height="11" viewBox="0 0 11 11"><rect x="0.5" y="0.5" width="10" height="10" rx="1" fill="none" stroke="var(--icon)"/><rect x="2" y="2" width="3" height="7" fill="var(--icon)"/><rect x="6" y="3" width="3" height="1.2" fill="var(--icon)"/><rect x="6" y="5.2" width="3" height="1.2" fill="var(--icon)"/><rect x="6" y="7.4" width="3" height="1.2" fill="var(--icon)"/></svg>
      (215) 555-0172
    </div>
    <div class="office-address">
      <svg width="11" height="11" viewBox="0 0 11 11"><rect width="11" height="11" rx="1.5" fill="var(--icon)"/><path d="M5.5 2a2.3 2.3 0 0 1 2.3 2.3c0 1.6-2.3 4.4-2.3 4.4S3.2 5.9 3.2 4.3A2.3 2.3 0 0 1 5.5 2z" fill="#fff"/></svg>
      <span>2250 Arch Street,<br>Suite 840, Philadelphia, PA 19103</span>
    </div>
  </section>

  <section class="office office--nj">
    <h2 class="office-title">NEW JERSEY</h2>
    <div class="office-line">
      <svg width="11" height="11" viewBox="0 0 11 11"><rect width="11" height="11" rx="1.5" fill="var(--icon)"/><path d="M6.8 2.5c-1.8 0.4-2.6 1.7-2.6 3s0.8 2.6 2.6 3" stroke="#fff" stroke-width="1.4" fill="none"/></svg>
      (856) 555-0118
    </div>
    <div class="office-line">
      <svg width="11" height="11" viewBox="0 0 11 11"><rect x="0.5" y="0.5" width="10" height="10" rx="1" fill="none" stroke="var(--icon)"/><rect x="2" y="2" width="3" height="7" fill="var(--icon)"/><rect x="6" y="3" width="3" height="1.2" fill="var(--icon)"/><rect x="6" y="5.2" width="3" height="1.2" fill="var(--icon)"/><rect x="6" y="7.4" width="3" height="1.2" fill="var(--icon)"/></svg>
      (856) 555-0193
    </div>
    <div class="office-address">
      <svg width="11" height="11" viewBox="0 0 11 11"><rect width="11" height="11" rx="1.5" fill="var(--icon)"/><path d="M5.5 2a2.3 2.3 0 0 1 2.3 2.3c0 1.6-2.3 4.4-2.3 4.4S3.2 5.9 3.2 4.3A2.3 2.3 0 0 1 5.5 2z" fill="#fff"/></svg>
      <span>615 Haddon Avenue,<br>Suite 310, Cherry Hill, NJ 08034</span>
    </div>
  </section>

  <section class="recipient">
    <h1 class="recipient-name">Name Surname</h1>
    <p class="recipient-line">Senior Executive</p>
    <p class="recipient-line">Address goes here. Street, City, Country</p>
    <p class="recipient-line">contact@yourmail.com</p>
    <p class="recipient-line">000-987-654-321</p>
  </section>

  <article class="letter-body">
    <p>Lorem ipsum dolor sit amet, consectetur adipisicing elit, sed do eiusmod tempor incididunt ut labore et dolore magna aliqua. Ut enim ad minim veniam, quis nostrud exercitation ullamco laboris nisi ut aliquip ex ea commodo consequat. Duis aute irure dolor in reprehenderit in voluptate velit esse cillum dolore eu fugiat nulla pariatur. Excepteur sint occaecat cupidatat non proident, sunt in culpa qui officia deserunt mollit anim id est laborum. Sed ut perspiciatis unde omnis iste natus error sit voluptatem accusantium doloremque laudantium, totam rem aperiam, eaque ipsa quae ab illo inventore veritatis et quasi architecto beatae vitae dicta sunt explicabo. Nemo enim ipsam voluptatem quia voluptas sit aspernatur aut odit aut fugit, sed quia consequuntur magni dolores eos qui ratione voluptatem sequi nesciunt. Neque porro voluptatem sequi nesciunt. Nemo enim ipsam voluptatem quia voluptas.</p>
    <p>Lorem ipsum dolor sit amet, consectetur adipisicing elit, sed do eiusmod tempor incididunt ut labore et dolore magna aliqua. Ut enim ad minim veniam, quis nostrud exercitation ullamco laboris nisi ut aliquip ex ea commodo consequat. Duis aute irure dolor in reprehenderit in voluptate velit esse cillum dolore eu fugiat nulla pariatur. Excepteur sint occaecat cupidatat non proident, sunt in culpa qui officia deserunt mollit anim id est laborum. Sed ut perspiciatis unde omnis iste natus error sit voluptatem accusantium doloremque laudantium, totam rem aperiam, eaque ipsa quae ab illo inventore veritatis et quasi architecto beatae vitae dicta sunt explicabo. Nemo enim ipsam voluptatem quia voluptas sit aspernatur aut odit aut.</p>
    <p>Lorem ipsum dolor sit amet, consectetur adipisicing elit, sed do eiusmod tempor incididunt ut labore et dolore magna aliqua. Ut enim ad minim veniam, quis nostrud exercitation ullamco laboris nisi ut aliquip ex ea commodo consequat. .</p>
  </article>

  <section class="sign-off">
    <div class="signature">Namesurename</div>
    <div class="signer-name">NAME SURNAME</div>
    <div class="signer-role">General Manager</div>
  </section>

  <div class="footer-rule"></div>
  <div class="footer-rule footer-rule--right"></div>
  <div class="footer-square"></div>

  <footer class="footer-contacts">
    <div class="footer-item">
      <svg width="20" height="20" viewBox="0 0 20 20"><circle cx="10" cy="10" r="9" fill="none" stroke="var(--icon)" stroke-width="1.2"/><circle cx="10" cy="10" r="5" fill="none" stroke="var(--icon)"/><ellipse cx="10" cy="10" rx="2.2" ry="5" fill="none" stroke="var(--icon)"/><path d="M5 10h10" stroke="var(--icon)"/></svg>
      www.hacpropertylaw.com
    </div>
    <div class="footer-item">
      <svg width="20" height="20" viewBox="0 0 20 20"><circle cx="10" cy="10" r="9" fill="none" stroke="var(--icon)" stroke-width="1.2"/><path d="M7 5.5l1.6 2.2-1 1.2c.6 1.3 1.5 2.2 2.8 2.8l1.2-1 2.2 1.6-.9 1.6c-3.2-.3-6.1-3.2-6.4-6.4z" fill="var(--icon)"/></svg>
      (215) 555-0140
    </div>
  </footer>
</main>
</body>
</html>
```